Price Package PDF - 2 page PDF of stylized price packages for property management firm

Looking for a 2 x A4 page PDF for our two price packages.
I would like this to be in similar style to our website www.harbourlanerentals.com.au
I have attached an example. But would like mine to be a little more stylish and modern, preferably using design similar to our website.
Words and images also attached

Target Market(s)

investment property owners, male and female, aged 30-60

Industry/Entity Type

Real Estate

Font styles to use
Sans Serif

Requirements
Must have
• split two packages onto seperate A4 pages (See example file attached)
• Contact info:
• Website: www.harbourlanerentals.com.au
• email: info@harbourlanerentals.com.au
• Phone: Tom Radley 0417 562 903, Larisa Okonjo 0409 317 648
• Office Address: Suite 7, 12-14 Wattle Parade, Curl Curl NSW 2096
Nice to have
• I would like to use any of the pictures provided or images of modern residential property interior or of Sydney's Northern Beaches.

```html
<!DOCTYPE html>
<html lang="en">
<head>
<meta charset="utf-8">
<title>Harbour Lane Rentals – Price Packages</title>
<link href="https://fonts.googleapis.com/css2?family=Source+Sans+3:wght@300;400;600&display=swap" rel="stylesheet">
<style>
:root{
  --teal:#2fa0a3;
  --teal-deep:#1c6e73;
  --teal-head:#2a94a0;
  --ink:#3a3e44;
  --muted:#6b7076;
  --footer:#353940;
  --table-bg:#e8e9ea;
  --stage:#ecebe8;
  --white:#ffffff;
}
*{box-sizing:border-box;margin:0;padding:0}
html,body{width:1200px;height:894px;overflow:hidden}
body{background:var(--stage);font-family:"Source Sans 3",sans-serif;color:var(--ink);position:relative}
.sheet{position:absolute;width:493px;height:698px;background:var(--white);box-shadow:0 4px 14px rgba(0,0,0,.18);overflow:hidden}
.sheet--all{left:84px;top:75px}
.sheet--lease{left:630px;top:120px}
.hero{position:absolute;left:0;top:0;width:493px;height:313px}
.hero-photo{position:absolute;inset:0}
.sheet--all .hero-photo{background:linear-gradient(180deg,#2c8fd0 0%,#6fb7df 30%,#c9c3b3 48%,#4f7a3c 70%,#2f4d2a 100%)}
.sheet--lease .hero-photo{background:linear-gradient(180deg,#1f86c8 0%,#5aa9d6 25%,#2e3a3e 50%,#4e7d3a 72%,#6b7f5a 100%)}
.title-band{position:absolute;left:0;bottom:0;width:100%;height:54px;background:rgba(24,104,108,.88);display:flex;align-items:center;justify-content:center}
.title-band h1{color:var(--white);font-weight:400;font-size:22px;letter-spacing:1.2px}
.includes{position:absolute;left:20px;top:326px;width:225px}
.includes h2{font-size:12.5px;font-weight:400;color:var(--teal-head);margin-bottom:6px}
.includes ul{list-style:none}
.includes li{position:relative;padding-left:9px;font-size:9.4px;line-height:14.6px}
.includes li::before{content:"";position:absolute;left:0;top:5px;width:4.5px;height:4.5px;border-radius:50%;background:var(--teal)}
.side{position:absolute;left:247px;top:332px;width:238px}
.thumbs{display:flex;gap:5px;height:71px}
.thumb{flex:1}
.thumb--a{background:linear-gradient(180deg,#3d8fcf,#7a8a86 60%,#3c5a6a)}
.thumb--b{background:linear-gradient(180deg,#1e73c2,#3f8fd0 55%,#2a5f8a)}
.thumb--c{background:linear-gradient(180deg,#2b7cc8,#8ab9d4 45%,#3b8d8c)}
.thumb--d{background:linear-gradient(180deg,#9fb8c8,#c9b98f 50%,#6f8d9c)}
.thumb--e{background:linear-gradient(180deg,#1c62b0,#3b84c6 60%,#27507a)}
.thumb--f{background:linear-gradient(180deg,#4a8fc0,#d8dde0 50%,#7c8a93)}
.package-bar{margin-top:6px;height:28px;background:var(--teal);color:var(--white);font-size:10.5px;display:flex;align-items:center;padding-left:12px}
.rates{margin-top:8px;background:var(--table-bg);padding:5px 6px 5px}
.rates table{width:100%;border-collapse:separate;border-spacing:0 4px}
.rates td{background:var(--white);font-size:6.2px;color:var(--muted);height:15px;padding:0 5px}
.rates td:first-child{width:122px}
.rates tr.lead td{color:var(--ink);font-weight:600}
.rates small{font-size:4px;font-weight:400}
.strip{position:absolute;left:0;top:622px;width:100%;height:6px;background:var(--teal)}
.footer{position:absolute;left:0;top:628px;width:100%;height:70px;background:var(--footer);color:var(--white)}
.brand{position:absolute;left:28px;top:24px;display:flex;align-items:center;gap:7px;font-size:13.5px;font-weight:600;letter-spacing:.3px}
.brand-dot{width:9px;height:9px;border-radius:50%;background:var(--teal)}
.contact{position:absolute;left:277px;top:17px;font-size:7.6px;line-height:9.2px}
</style>
</head>
<body>

<section class="sheet sheet--all">
  <div class="hero">
    <div class="hero-photo" role="img" aria-label="Row of modern terraced houses with landscaped gardens under a blue sky"></div>
    <div class="title-band"><h1>ALL INCLUSIVE PACKAGE</h1></div>
  </div>
  <div class="includes">
    <h2>INCLUDES:</h2>
    <ul>
      <li>Securing Tenant</li>
      <li>Reference/Database Checking</li>
      <li>Lease Preparation and Signing</li>
      <li>Direct Debit rent collection</li>
      <li>Zero arrears policy management</li>
      <li>Payment of Rates and levies</li>
      <li>Insurance management</li>
      <li>Coordination or all repairs and maintenance</li>
      <li>Regular rent reviews and renewals</li>
      <li>Detailed ingoing, ongoing and outgoing inspections with photos and videos – viewable through your personal Landlord portal</li>
      <li>Bond management – lodging and refunding</li>
      <li>Electronic monthly and EOFY statements</li>
      <li>Annual scheduled maintenance report</li>
      <li>Regulation/compliance management</li>
      <li>Tribunal Representation</li>
    </ul>
  </div>
  <div class="side">
    <div class="thumbs">
      <div class="thumb thumb--a" role="img" aria-label="Waterfront promenade with cafés"></div>
      <div class="thumb thumb--b" role="img" aria-label="Boats moored in a harbour"></div>
      <div class="thumb thumb--c" role="img" aria-label="Rock pool by the ocean"></div>
    </div>
    <div class="package-bar">All Inclusive Package</div>
    <div class="rates">
      <table>
        <tr class="lead"><td>Management Rate:</td><td>10% <small>+ GST of rental income</small></td></tr>
        <tr><td>Letting Fee:</td><td>No Charge</td></tr>
        <tr><td>Advertising:</td><td>No Charge</td></tr>
        <tr><td>Professional Photography:</td><td>$199 <small>(inc GST)</small> 4 x Photos</td></tr>
        <tr><td>Statements:</td><td>No Charge</td></tr>
        <tr><td>Lease Preperation:</td><td>No Charge</td></tr>
        <tr><td>Renewal Fees:</td><td>No Charge</td></tr>
      </table>
    </div>
  </div>
  <div class="strip"></div>
  <footer class="footer">
    <div class="brand"><span>HARBOUR LANE</span><span class="brand-dot"></span></div>
    <address class="contact" style="font-style:normal">
      Tom Radley 0417 562 903 &nbsp;|&nbsp; Larisa Okonjo 0409 317 648<br>
      Suite 7, 12-14 Wattle Parade, Curl Curl NSW 2096<br>
      info@harbourlanerentals.com.au<br>
      www.harbourlanerentals.com.au
    </address>
  </footer>
</section>

<section class="sheet sheet--lease">
  <div class="hero">
    <div class="hero-photo" role="img" aria-label="Modern two-storey home with balconies above a leafy garden"></div>
    <div class="title-band"><h1>LEASE AND MANAGEMENT PACKAGE</h1></div>
  </div>
  <div class="includes">
    <h2>INCLUDES:</h2>
    <ul>
      <li>Securing Tenant</li>
      <li>Reference/Database Checking</li>
      <li>Lease Preparation and Signing</li>
      <li>Direct Debit rent collection</li>
      <li>Zero arrears policy management</li>
      <li>Payment of Rates and levies</li>
      <li>Insurance management</li>
      <li>Coordination or all repairs and maintenance</li>
      <li>Regular rent reviews and renewals</li>
      <li>Detailed ingoing, ongoing and outgoing inspections with photos and videos – viewable through your personal Landlord portal</li>
      <li>Bond management – lodging and refunding</li>
      <li>Electronic monthly and EOFY statements</li>
      <li>Annual scheduled maintenance report</li>
      <li>Regulation/compliance management</li>
      <li>Tribunal Representation</li>
    </ul>
  </div>
  <div class="side">
    <div class="thumbs">
      <div class="thumb thumb--d" role="img" aria-label="Beachfront apartments across calm water"></div>
      <div class="thumb thumb--e" role="img" aria-label="Boats in a deep blue bay"></div>
      <div class="thumb thumb--f" role="img" aria-label="Wharf building against the sky"></div>
    </div>
    <div class="package-bar">Management Rate</div>
    <div class="rates">
      <table>
        <tr class="lead"><td>Management Rate:</td><td>6% <small>+ GST of rental income</small></td></tr>
        <tr><td>Letting Fee:</td><td>1 weeks rent+GST 6 or 12 month lease</td></tr>
        <tr><td>Advertising:</td><td>$350 <small>(inc GST)</small></td></tr>
        <tr><td>Professional Photography:</td><td>$199 <small>(inc GST)</small> 4 x Photos</td></tr>
        <tr><td>Statements:</td><td>$5.00 Per month</td></tr>
        <tr><td>Lease Preperation:</td><td>No Charge</td></tr>
        <tr><td>Renewal Fees:</td><td>½ Weeks Rent +GST</td></tr>
      </table>
    </div>
  </div>
  <div class="strip"></div>
  <footer class="footer">
    <div class="brand"><span>HARBOUR LANE</span><span class="brand-dot"></span></div>
    <address class="contact" style="font-style:normal">
      Tom Radley 0417 562 903 &nbsp;|&nbsp; Larisa Okonjo 0409 317 648<br>
      Suite 7, 12-14 Wattle Parade, Curl Curl NSW 2096<br>
      info@harbourlanerentals.com.au<br>
      www.harbourlanerentals.com.au
    </address>
  </footer>
</section>

</body>
</html>
```